Health and Wellness company needs flyer to promote free seminar

Stride reform studio is a health and wellness company that offers an exercise program designed by physical therapists to help relieve pain and improve mobility. Our business is a new concept that is not well understood by the public. In order to promote our business we offer a free seminar where we present information regarding the underlying cause of pain and tightness. During the seminar we also perform a posture screen and movement testing for all participants.

Target Market(s)

Mostly healthy and active women ages 25-65

Industry/Entity Type

Health And Wellness

Font styles to use
Sans Serif

Colors

Designer to choose colors to be used in the design.

Requirements
Must have
• Title: Eliminate Pain and Tightness For Good
• Paragraph: Stride Reform Studio offers a free 60 minute seminar: "The Busy Walker's Handbook to Bending and Standing Taller."
• What to Expect:
• • Identify the underlying cause of your pain and mobility issues
• • Expose what gets in the way of you moving and feeling better
• • Learn why traditional exercises don’t help and can actually make the problem worse
• • Reveal what your posture is saying and how that impacts you
• • Experience your muscle imbalances through movement tests
• • Discover the training method that realigns your posture, increases your mobility and reduces your pain
• Call to action: RSVP online at stridereformstudio.com
Nice to have
• Use a relevant image showing a female dealing with tightness in the low back, legs, etc.
• Emphasize that the seminar is FREE.
• Make the call to action prominent.

```html
<!DOCTYPE html>
<html lang="en">
<head>
<meta charset="utf-8">
<title>Stride Reform Studio – Free Seminar Flyer</title>
<link rel="stylesheet" href="https://fonts.googleapis.com/css2?family=Oswald:wght@300;400;500;600;700&family=Open+Sans:wght@300;400;600&display=swap">
<style>
:root{
  --navy:#2b2f6b;
  --navy-deep:#151a3d;
  --navy-stripe:#343d93;
  --orange:#ff7a00;
  --orange-deep:#f05a00;
  --paper:#eeeeee;
  --ink:#222;
  --photo:#0f1219;
  --white:#fff;
}
*{margin:0;padding:0;box-sizing:border-box}
html,body{width:967px;height:1200px;overflow:hidden;background:var(--paper)}
.flyer{position:relative;width:967px;height:1200px;overflow:hidden;font-family:'Open Sans',sans-serif;color:var(--ink);background:var(--photo)}
.hero-photo{position:absolute;left:0;top:222px;width:967px;height:817px;
  background:
    radial-gradient(ellipse 120px 60px at 880px 700px,rgba(150,45,40,.75),rgba(150,45,40,0) 100%),
    radial-gradient(ellipse 70px 50px at 555px 370px,rgba(40,70,170,.7),rgba(40,70,170,0) 100%),
    radial-gradient(ellipse 110px 150px at 850px 480px,rgba(185,130,105,.55),rgba(185,130,105,0) 100%),
    radial-gradient(ellipse 150px 90px at 680px 440px,rgba(170,115,90,.5),rgba(170,115,90,0) 100%),
    radial-gradient(ellipse 130px 140px at 500px 290px,rgba(70,70,78,.8),rgba(70,70,78,0) 100%),
    radial-gradient(ellipse 180px 200px at 860px 620px,rgba(45,42,44,.9),rgba(45,42,44,0) 100%),
    radial-gradient(ellipse at 70% 50%,#262630 0%,#15171e 45%,#0b0d12 85%)}
.shapes{position:absolute;inset:0}
.headline{position:absolute;left:213px;top:22px;font-family:'Oswald',sans-serif;font-weight:700;font-size:120px;line-height:1;letter-spacing:4px;background:linear-gradient(180deg,#f4f4f4 0%,#b9b9b9 45%,#e6e6e6 60%,#8f8f8f 100%);-webkit-background-clip:text;background-clip:text;color:transparent}
.subhead{position:absolute;left:251px;top:138px;font-family:'Oswald',sans-serif;font-weight:300;font-size:57px;line-height:1;color:#e9e9e9;letter-spacing:2.6px;white-space:nowrap}
.free-badge{position:absolute;left:760px;top:0;width:172px;height:122px}
.free-badge .free{position:absolute;left:0;right:0;top:24px;text-align:center;font-family:'Oswald',sans-serif;font-weight:600;font-size:46px;line-height:1;color:var(--white)}
.free-badge .free sup{font-size:20px;vertical-align:top;position:relative;top:2px}
.free-badge .invite{position:absolute;left:0;right:0;top:76px;text-align:center;font-family:'Oswald',sans-serif;font-weight:500;font-size:16px;color:var(--white)}
.brand{position:absolute;left:36px;top:380px;display:flex;align-items:center;gap:12px;font-family:'Open Sans',sans-serif;font-weight:600;font-size:28px;color:var(--navy)}
.brand .mark{width:24px;height:24px;background:var(--orange)}
.why-title{position:absolute;left:36px;top:458px;font-family:'Oswald',sans-serif;font-weight:600;font-size:38px;letter-spacing:3px;color:var(--white);line-height:44px}
.intro{position:absolute;left:36px;top:538px;width:540px;color:var(--white)}
.intro .lead{font-size:14px;text-transform:uppercase;text-align:center;width:500px;line-height:18px}
.intro .guide{font-family:'Oswald',sans-serif;font-weight:500;font-size:17px;line-height:22px;text-align:center;width:500px;margin-top:7px;text-transform:uppercase;white-space:nowrap}
.intro .story{font-size:15px;line-height:21px;margin-top:12px;width:500px}
.pose-photo{position:absolute;left:30px;top:700px;width:195px;height:335px;
  background:
    radial-gradient(ellipse 40px 35px at 120px 300px,rgba(205,160,135,.6),rgba(205,160,135,0) 100%),
    radial-gradient(ellipse 55px 30px at 105px 280px,rgba(255,255,255,.9),rgba(255,255,255,0) 100%),
    radial-gradient(ellipse 35px 110px at 80px 150px,rgba(70,66,62,.55),rgba(70,66,62,0) 100%),
    radial-gradient(ellipse 25px 40px at 105px 30px,rgba(215,180,160,.5),rgba(215,180,160,0) 100%)}
.expect-title{position:absolute;left:270px;top:711px;font-family:'Oswald',sans-serif;font-weight:400;font-size:40px;line-height:46px;color:#111}
.expect-title span{color:var(--orange);font-weight:600}
.expect-list{position:absolute;left:272px;top:764px;width:445px;list-style:none}
.expect-list li{position:relative;padding-left:20px;font-size:16px;font-weight:300;line-height:19px;height:44.6px}
.expect-list li::before{content:"";position:absolute;left:0;top:4px;width:10px;height:10px;border:2px solid var(--navy-stripe);background:var(--orange)}
.expect-list b{font-weight:400}
.studio{position:absolute;top:1052px;color:var(--white)}
.studio h3{font-family:'Oswald',sans-serif;font-weight:300;font-size:24px;line-height:30px}
.studio h3 span{color:var(--orange);font-weight:500}
.studio .line{display:flex;gap:5px;font-size:13px;line-height:16px;margin-top:4px}
.studio .line svg{flex:none;margin-top:2px}
.studio .note{font-size:10.5px;line-height:13px;margin-top:10px;width:295px}
.houston{left:36px}
.portland{left:351px}
.cta{position:absolute;left:687px;top:1098px;width:171px;height:26px;border-radius:13px;background:var(--orange);color:var(--white);font-family:'Oswald',sans-serif;font-weight:500;font-size:19px;line-height:26px;text-align:center}
.cta-url{position:absolute;left:658px;top:1129px;width:230px;text-align:center;font-size:10px;font-weight:600;color:var(--white)}
</style>
</head>
<body>
<div class="flyer">
  <div class="hero-photo" role="img" aria-label="Photo of a woman doing a leg press in a dark gym"></div>

  <svg class="shapes" width="967" height="1200" viewBox="0 0 967 1200" aria-hidden="true">
    <defs>
      <linearGradient id="hdr" x1="0" y1="0" x2="0" y2="1">
        <stop offset="0" stop-color="#2e3476"/><stop offset="1" stop-color="#1c2150"/>
      </linearGradient>
      <linearGradient id="foot" x1="0" y1="0" x2="0" y2="1">
        <stop offset="0" stop-color="#1d2150"/><stop offset="1" stop-color="#0f1230"/>
      </linearGradient>
    </defs>
    <rect x="0" y="0" width="967" height="222" fill="url(#hdr)"/>
    <polygon points="0,0 122,0 265,222 232,222 0,30" fill="var(--orange)"/>
    <polygon points="0,0 70,0 240,222 232,222 0,30" fill="var(--orange-deep)"/>
    <polygon points="250,222 290,222 440,504 400,504" fill="var(--navy-stripe)"/>
    <polygon points="0,30 232,222 250,222 400,504 0,504" fill="var(--paper)"/>
    <polygon points="0,504 430,504 652,698 0,698" fill="var(--navy)"/>
    <polygon points="430,504 470,504 692,698 652,698" fill="var(--navy-stripe)"/>
    <polygon points="0,455 380,455 406,504 0,504" fill="var(--orange-deep)"/>
    <polygon points="652,698 692,698 880,1039 840,1039" fill="var(--navy-stripe)"/>
    <polygon points="0,698 652,698 840,1039 0,1039" fill="var(--paper)"/>
    <rect x="0" y="1039" width="967" height="161" fill="url(#foot)"/>
    <polygon points="870,1039 967,1039 967,1200 950,1200" fill="var(--orange)"/>
    <polygon points="905,1039 967,1039 967,1150" fill="var(--orange-deep)"/>
    <polygon points="760,0 932,0 932,96 846,122 760,96" fill="var(--orange)"/>
  </svg>

  <div class="pose-photo" role="img" aria-label="Photo of a man in a shoulder-stand stretch"></div>

  <h1 class="headline">ELIMINATE</h1>
  <p class="subhead">PAIN &amp; TIGHTNESS FOR GOOD</p>

  <div class="free-badge">
    <div class="free"><sup>*</sup>FREE</div>
    <div class="invite">SEMINAR INVITATION</div>
  </div>

  <div class="brand"><span class="mark"></span>Stride reform studio</div>

  <h2 class="why-title">WHY CHOOSE US</h2>

  <div class="intro">
    <p class="lead">Stride Reform Studio offers a free 60 minute seminar</p>
    <p class="guide">" The Busy Walker's Handbook to Bending and Standing Taller "</p>
    <p class="story">Stride Reform Studio is the creation of Rosa Lindqvist &amp; Theo Barrand, two physical therapists who were frustrated with the medical system. Being forced to treat symptoms with limited appointments.</p>
  </div>

  <h2 class="expect-title">WHAT TO <span>EXPECT</span></h2>
  <ul class="expect-list">
    <li><b>Identify</b> the underlying cause of your pain &amp; mobility issues.</li>
    <li><b>Expose</b> what gets in the way of you moving &amp; feeling better.</li>
    <li><b>Learn</b> why traditional exercises don’t help &amp; can actually make the problem worse.</li>
    <li><b>Reveal</b> what your posture is saying &amp; how that impacts you.</li>
    <li><b>Experience</b> your muscle imbalances through movement tests.</li>
    <li><b>Discover</b> the training method that realigns your posture, increases your mobility and reduces your pain.</li>
  </ul>

  <div class="studio houston">
    <h3>STUDIO <span>HOUSTON</span></h3>
    <div class="line"><svg width="8" height="11" viewBox="0 0 8 11"><path d="M4 0.5a3.5 3.5 0 0 1 3.5 3.5C7.5 6.5 4 10.5 4 10.5S0.5 6.5 0.5 4A3.5 3.5 0 0 1 4 0.5z" fill="none" stroke="#fff" stroke-width="1.2"/><circle cx="4" cy="4" r="1.2" fill="#fff"/></svg><span>1480 Alder Lane,<br>Houston, TX 77000</span></div>
    <div class="line" style="margin-top:10px"><svg width="9" height="10" viewBox="0 0 9 10"><path d="M2 0.5 3.5 3 2.5 4.2C3.2 5.8 4.2 6.8 5.8 7.5L7 6.5 9 8 8 9.5C4 9.5 0.5 6 0.5 1.5z" fill="#fff"/></svg><span>(281) 555-0147</span></div>
    <p class="note">Located inside Keystone Dance Loft with off-street parking located in front of the building.</p>
  </div>

  <div class="studio portland">
    <h3>STUDIO <span>PORTLAND</span></h3>
    <div class="line"><svg width="8" height="11" viewBox="0 0 8 11"><path d="M4 0.5a3.5 3.5 0 0 1 3.5 3.5C7.5 6.5 4 10.5 4 10.5S0.5 6.5 0.5 4A3.5 3.5 0 0 1 4 0.5z" fill="none" stroke="#fff" stroke-width="1.2"/><circle cx="4" cy="4" r="1.2" fill="#fff"/></svg><span>5820 SE Harbor Road #210<br>Milwaukie, OR 97200</span></div>
    <div class="line" style="margin-top:10px"><svg width="9" height="10" viewBox="0 0 9 10"><path d="M2 0.5 3.5 3 2.5 4.2C3.2 5.8 4.2 6.8 5.8 7.5L7 6.5 9 8 8 9.5C4 9.5 0.5 6 0.5 1.5z" fill="#fff"/></svg><span>(503) 555-0192</span></div>
    <p class="note">Located in Downtown Milwaukie across from the Riverside light rail stop. Off-street parking lot in the back.</p>
  </div>

  <div class="cta">SIGN UP ONLINE</div>
  <div class="cta-url">stridereformstudio.com/free-seminar</div>
</div>
</body>
</html>
```